"Drink Champagne and Dance on the Table" sort of business card needed!

We throw events, weddings, engagement parties, baby showers and the sort of end of year corporate events that people remember long after the glitter has settled - the sort of events that make you stand still and say wow when you walk in and then make you want to "Drink Champagne and Dance on the Tables"

We have a great logo with heaps of potential and need a business card that just screams creative professionals!

We are based in Auckland, NZ and are priced at the Premium end of the market were there are around 10 other main competitors. We need to stand out and make a strong statement about who we are!

Our Business Card will be one of the few items that we print out so are fully prepared to invest in a premium print job.

We really love our logo and think it has heaps of potential! Its ok if you would like to manipulate it (maybe put it on an angle, or use the circle element on its own?).

Black and Gold is very striking, but its very done in our market so we would like to avoid a solid black background please

We have done a bit of an inspiration document to give you an idea of the sort of look and feel we are hoping to achieve.

Target Market(s)

Woman aged 30 - 45 with an income bracket of $70k +

Industry/Entity Type

Event Planning

Contact Information for Business Card

Marnie
hello@fennoriwick.co.nz
www.fennoriwick.co.nz
02734419027

Number of Pages Required

5+ page

Requirements
Must have
• Vibrant colours and design (we love the vibrant pink and gold in the inspiration file)
• We would love to see some colour and creativity (although the black and gold is very striking). Because we are doing such minimal print work I am happy for the cards to be a little more expensive so if you want to use cut outs, rounded corners, gold foil, non standard size etc I am happy for that too. I really want the wow factor.
Nice to have
• We would like the design to be double sided.
Should not have
• The logo colour changed
• Use of Purple or Green or solid black background.
• Wedding Photos!

```html
<!DOCTYPE html>
<html lang="en">
<head>
<meta charset="utf-8">
<title>Fenn and Oriwick — Business Card</title>
<link rel="stylesheet" href="https://fonts.googleapis.com/css2?family=Russo+One&family=Libre+Baskerville:wght@400;700&display=swap">
<style>
  :root {
    --pink: #c81d5e;
    --pink-light: #e0658f;
    --gold: #d9a521;
    --gold-light: #f3d36a;
    --black: #1c1a1b;
    --backdrop: #eceeef;
  }
  * { margin: 0; padding: 0; box-sizing: border-box; }
  html, body {
    width: 1200px; height: 900px; overflow: hidden;
    background: var(--backdrop);
  }
  .canvas {
    width: 1200px; height: 900px;
    display: flex; flex-direction: column;
    align-items: center; justify-content: center; gap: 60px;
  }
  .card {
    position: relative;
    width: 560px; height: 320px;
    overflow: hidden;
    box-shadow: 0 10px 30px rgba(0,0,0,.18);
  }
  .card > .card-art { position: absolute; inset: 0; display: block; }

  /* Brand side */
  .brand-lockup {
    position: absolute; top: 34px; right: 36px;
    display: flex; align-items: center; gap: 12px;
    color: var(--gold);
  }
  .brand-mark {
    width: 44px; height: 44px; border-radius: 50%;
    border: 2px solid var(--gold);
    flex: none;
  }
  .brand-text { display: flex; flex-direction: column; align-items: stretch; }
  .brand-name {
    font-family: "Libre Baskerville", serif; font-weight: 700;
    font-size: 22px; letter-spacing: .5px; line-height: 1.1;
  }
  .brand-tagline {
    font-family: "Libre Baskerville", serif; font-weight: 400;
    font-size: 8px; letter-spacing: 3px; margin-top: 4px;
    border-top: 1px solid var(--gold); padding-top: 3px;
    text-align: center;
  }

  /* Contact side */
  .person-name {
    position: absolute; left: 150px; top: 86px;
    font-family: "Russo One", sans-serif; font-weight: 400;
    font-size: 46px; line-height: 50px; letter-spacing: 4px;
    color: var(--black); text-transform: uppercase;
  }
  .contact-list {
    position: absolute; left: 190px; top: 163px;
    list-style: none;
    font-family: "Libre Baskerville", serif;
    font-size: 15px; color: var(--gold-light);
  }
  .contact-list li {
    display: flex; align-items: center; gap: 12px;
    height: 29px; white-space: nowrap;
  }
  .contact-icon { width: 18px; height: 18px; flex: none; display: block; }
</style>
</head>
<body>
<main class="canvas">

  <section class="card card-brand">
    <svg class="card-art" viewBox="0 0 560 320" width="560" height="320" aria-hidden="true">
      <defs>
        <radialGradient id="brandSheen" cx="0.45" cy="0.55" r="0.7">
          <stop offset="0" stop-color="#d8457a"/>
          <stop offset="1" stop-color="#c81d5e"/>
        </radialGradient>
        <linearGradient id="goldSweep" x1="0" x2="1">
          <stop offset="0" stop-color="#b07b12"/>
          <stop offset=".45" stop-color="#f3d36a"/>
          <stop offset="1" stop-color="#c8911a"/>
        </linearGradient>
        <linearGradient id="blackSweep" x1="0" y1="0" x2="1" y2="1">
          <stop offset="0" stop-color="#2a2728"/>
          <stop offset="1" stop-color="#0e0d0d"/>
        </linearGradient>
      </defs>
      <rect width="560" height="320" fill="url(#brandSheen)"/>
      <path d="M0,170 Q280,300 560,60" fill="none" stroke="#f07aa3" stroke-opacity=".35" stroke-width="26"/>
      <path d="M0,205 Q300,330 560,95 L560,320 L0,320 Z" fill="url(#blackSweep)"/>
      <path d="M0,200 Q300,325 560,90" fill="none" stroke="url(#goldSweep)" stroke-width="9"/>
      <path d="M0,260 Q320,340 560,160" fill="none" stroke="#3a3637" stroke-width="14" stroke-opacity=".6"/>
    </svg>
    <div class="brand-lockup">
      <span class="brand-mark"></span>
      <div class="brand-text">
        <span class="brand-name">Fenn and Oriwick</span>
        <span class="brand-tagline">WEDDINGS &amp; EVENTS</span>
      </div>
    </div>
  </section>

  <section class="card card-contact">
    <svg class="card-art" viewBox="0 0 560 320" width="560" height="320">
      <defs>
        <linearGradient id="goldRule" x1="0" x2="1">
          <stop offset="0" stop-color="#b07b12"/>
          <stop offset=".5" stop-color="#f3d36a"/>
          <stop offset="1" stop-color="#c8911a"/>
        </linearGradient>
        <radialGradient id="confettiTone" cx="1" cy="0" r="1.1" gradientTransform="scale(1 1)">
          <stop offset="0" stop-color="#e2b23a" stop-opacity=".75"/>
          <stop offset=".35" stop-color="#d9a521" stop-opacity=".35"/>
          <stop offset=".75" stop-color="#c81d5e" stop-opacity="0"/>
        </radialGradient>
      </defs>
      <rect width="560" height="320" fill="var(--pink)"/>
      <rect class="confetti-area" role="img" aria-label="Scattered gold confetti dots across the pink top" x="0" y="0" width="560" height="138" fill="url(#confettiTone)"/>
      <rect y="138" width="560" height="7" fill="url(#goldRule)"/>
      <rect y="145" width="560" height="124" fill="var(--black)"/>
      <rect y="269" width="560" height="7" fill="url(#goldRule)"/>
      <rect y="300" width="560" height="3" fill="var(--black)"/>
    </svg>
    <h1 class="person-name">Marnie</h1>
    <ul class="contact-list">
      <li>
        <svg class="contact-icon" viewBox="0 0 18 18" aria-hidden="true"><rect x="2" y="4" width="14" height="10" fill="none" stroke="#d9a521" stroke-width="1.4"/><path d="M2 4 L9 10 L16 4" fill="none" stroke="#d9a521" stroke-width="1.4"/></svg>
        <span>hello@fennoriwick.co.nz</span>
      </li>
      <li>
        <svg class="contact-icon" viewBox="0 0 18 18" aria-hidden="true"><circle cx="9" cy="9" r="7" fill="none" stroke="#d9a521" stroke-width="1.4"/><ellipse cx="9" cy="9" rx="3" ry="7" fill="none" stroke="#d9a521" stroke-width="1.2"/><path d="M2 9 H16" stroke="#d9a521" stroke-width="1.2"/></svg>
        <span>www.fennoriwick.co.nz</span>
      </li>
      <li>
        <svg class="contact-icon" viewBox="0 0 18 18" aria-hidden="true"><circle cx="9" cy="9" r="8" fill="none" stroke="#d9a521" stroke-width="1.4"/><path d="M6 5 L7.5 5 L8.3 7.2 L7.2 8 Q8 10 10 10.8 L10.8 9.7 L13 10.5 L13 12 Q10 13.5 7 10.8 Q4.5 8 6 5 Z" fill="#d9a521"/></svg>
        <span>02734419027</span>
      </li>
    </ul>
  </section>

</main>
</body>
</html>
```